Goat cheese label

See attached label. I want a label very similar with my information substituted. Hares N Heron Acres, Goat's Milk Chèvre, HaresNHeronAcres@mailwell.net, will need 4 oz and 16oz labels

```html
<!DOCTYPE html>
<html lang="en">
<head>
<meta charset="utf-8">
<title>Hares N Heron Acres – Goat's Milk Chèvre Labels</title>
<link rel="stylesheet" href="https://fonts.googleapis.com/css2?family=Oswald:wght@500;700&family=Pathway+Gothic+One&family=Tinos:wght@700&family=Arimo:wght@700&display=swap">
<style>
  :root {
    --sheet-white: #ffffff;
    --sheet-orange: #f9ae42;
    --rule-grey: #c9c9c9;
    --rule-orange: #e89a35;
    --divider: #9a8a74;
    --ring-brown: #8a5a37;
    --field-tan: #c9a070;
    --field-tan-light: #dcc09a;
    --band-brown: #6e4425;
    --hill-green: #1f7d22;
    --hill-green-dark: #0c4a0e;
    --cheese-cream: #ece7dc;
    --ink-dark: #1b1b1b;
    --ink-brown: #2e1a0c;
    --ring-text: #ffffff;
    --bubble: #ffffff;
  }
  html, body {
    margin: 0;
    padding: 0;
    width: 1200px;
    height: 1200px;
    overflow: hidden;
    background: var(--sheet-white);
  }
  .label-sheet {
    display: block;
    width: 1200px;
    height: 1200px;
  }
  .sheet-top { fill: var(--sheet-white); }
  .sheet-bottom { fill: var(--sheet-orange); }
  .sheet-rule { stroke: var(--rule-grey); stroke-width: 3; }
  .sheet-rule-orange { stroke: var(--rule-orange); stroke-width: 3; }
  .sheet-divider { stroke: var(--divider); stroke-width: 1.5; }

  .label-ring { fill: var(--ring-brown); }
  .label-hills { fill: url(#hillGradient); }
  .label-band { fill: var(--band-brown); }
  .label-cheese { fill: var(--cheese-cream); }

  .farm-arc {
    font-family: "Oswald", "Arial Narrow", sans-serif;
    font-weight: 700;
    font-size: 56px;
    fill: var(--ring-text);
    letter-spacing: 1px;
  }
  .email-arc {
    font-family: "Arimo", Arial, sans-serif;
    font-weight: 700;
    font-size: 22px;
    fill: var(--ink-dark);
  }
  .farm-mark {
    font-family: "Oswald", "Arial Narrow", sans-serif;
    font-weight: 700;
    font-size: 48px;
    fill: var(--ink-dark);
    text-anchor: middle;
  }
  .product-name {
    font-family: "Pathway Gothic One", "Arial Narrow", sans-serif;
    font-size: 44px;
    fill: var(--ink-brown);
    text-anchor: middle;
  }
  .size-bubble { fill: var(--bubble); }
  .size-text {
    font-family: "Tinos", "Times New Roman", serif;
    font-weight: 700;
    font-size: 36px;
    fill: var(--ink-dark);
    text-anchor: middle;
  }
</style>
</head>
<body>
<svg class="label-sheet" viewBox="0 0 1200 1200" xmlns="http://www.w3.org/2000/svg" xmlns:xlink="http://www.w3.org/1999/xlink">
  <defs>
    <radialGradient id="fieldGradient" cx="50%" cy="40%" r="60%">
      <stop offset="0%" stop-color="var(--field-tan-light)"/>
      <stop offset="100%" stop-color="var(--field-tan)"/>
    </radialGradient>
    <linearGradient id="hillGradient" x1="0" y1="0" x2="0" y2="1">
      <stop offset="0%" stop-color="var(--hill-green)"/>
      <stop offset="100%" stop-color="var(--hill-green-dark)"/>
    </linearGradient>
    <clipPath id="fieldClip">
      <ellipse cx="0" cy="0" rx="262" ry="182" transform="rotate(-35)"/>
    </clipPath>
    <path id="farmNamePath" d="M -282 0 A 282 205 0 0 1 282 0" transform="rotate(-35)"/>
    <path id="emailPath" d="M -300 0 A 300 218 0 0 0 300 0" transform="rotate(-35)"/>

    <g id="labelBase">
      <ellipse class="label-ring" cx="0" cy="0" rx="330" ry="245" transform="rotate(-35)"/>
      <ellipse cx="0" cy="0" rx="262" ry="182" transform="rotate(-35)" fill="url(#fieldGradient)"/>
      <g clip-path="url(#fieldClip)">
        <rect class="label-hills" x="-320" y="30" width="640" height="120" role="img" aria-label="Green rolling hills scene"/>
        <rect class="label-band" x="-320" y="132" width="640" height="110" transform="rotate(-6)"/>
      </g>

      <text class="farm-arc"><textPath xlink:href="#farmNamePath" startOffset="50%" text-anchor="middle">Hares N Heron Acres</textPath></text>
      <text class="email-arc"><textPath xlink:href="#emailPath" startOffset="36%" text-anchor="middle">HaresNHeronAcres@mailwell.net</textPath></text>

      <text class="farm-mark" x="40" y="-70">Hares N Heron</text>
      <text class="farm-mark" x="40" y="-16">Acres</text>

      <rect class="label-cheese" x="-212" y="52" width="150" height="62" rx="26" role="img" aria-label="Wheel of white goat cheese with a wedge cut out"/>

      <text class="product-name" x="-58" y="178" transform="rotate(-6)">Goat's Milk Chèvre</text>
    </g>
  </defs>

  <rect class="sheet-top" x="0" y="0" width="1200" height="580"/>
  <rect class="sheet-bottom" x="0" y="580" width="1200" height="620"/>
  <line class="sheet-rule" x1="700" y1="16" x2="1200" y2="16"/>
  <line class="sheet-divider" x1="0" y1="580" x2="1200" y2="580"/>
  <line class="sheet-rule-orange" x1="0" y1="612" x2="560" y2="612"/>

  <g class="label label-16oz" transform="translate(855 290)">
    <use xlink:href="#labelBase"/>
    <ellipse class="size-bubble" cx="92" cy="80" rx="54" ry="32"/>
    <text class="size-text" x="92" y="92">16 oz</text>
  </g>

  <g class="label label-4oz" transform="translate(343 897)">
    <use xlink:href="#labelBase"/>
    <ellipse class="size-bubble" cx="92" cy="80" rx="50" ry="31"/>
    <text class="size-text" x="92" y="92">4 oz</text>
  </g>
</svg>
</body>
</html>
```